https://www.kreidetafel.de - a website for school website in germany for presentation/paper download

we own the webpage https://www.kreidetafel.de and we need a new webdesign (a new website logo is also possible). we want only new images and css, we don´t want to made any change to the HTML code.
we need only new images/color for a new modern look.

we want to have more trust to our user. they have to download presentation/paper
we need template for this sites:
https://www.kreidetafel.de/
https://www.kreidetafel.de/referate/englisch
https://www.kreidetafel.de/forum.php
https://www.kreidetafel.de/forum/insektenhotel/147503
https://www.kreidetafel.de/referat/latein/sokrates/14781
https://www.kreidetafel.de/schule_seminararbeit_fachliste.php?fach=127
and other sites on the website. (take a look around the website)

we don´t like white color for sublines or text. (h1/h2/strong) . in image are white Text OK.

important: we want to chance ONLY the CSS and PICS, we don´t want to remove or chance any HTML code.

after you have made a mockup of the new design and we give you a go, you have to made a package with the IMAGES and the CSS rules (text how we have to chance the current css)

Target Market(s)

Germany, Austria, Switzerland -DACH

Industry/Entity Type

School

Coding

Coded - Design and coding required

Number of Pages Required

5+ page

Font styles to use
Serif
Sans Serif

Colors

Designer to choose colors to be used in the design.

Requirements
Must have
• We want only to remove images and no HTML Code
Should not have
• NO white colors for Text on the site. In images are OK

```html
<!DOCTYPE html>
<html lang="de">
<head>
<meta charset="utf-8">
<title>Kreidetafel.de – Referate, Hausaufgaben und nette Leute kennen lernen</title>
<link rel="stylesheet" href="https://fonts.googleapis.com/css2?family=Alegreya:wght@400&family=Mulish:wght@400;500;600;700&display=swap">
<style>
:root{
  --lime:#cdd862;
  --lime-soft:#d4dc7e;
  --olive:#6b6f45;
  --ink:#3b3f24;
  --text:#45492d;
  --muted:#8b8d7a;
  --link:#3d6fa8;
  --panel:#f2f2e3;
  --panel-gray:#f3f3f1;
  --input:#e9ebc9;
  --button:#cfd68b;
  --line:#e2e2d4;
  --white:#ffffff;
}
*{box-sizing:border-box;margin:0;padding:0}
html,body{width:1200px;height:960px;overflow:hidden;background:var(--white)}
body{font-family:"Mulish",sans-serif;color:var(--text);font-size:11px;position:relative}
a{color:var(--link);text-decoration:none}
.page{position:absolute;left:216px;top:0;width:768px;height:960px;border-left:1px solid #e8e8e8;border-right:1px solid #e8e8e8}
.abs{position:absolute}

/* header */
.site-header{left:0;top:0;width:768px;height:121px;background:var(--lime)}
.brand{left:22px;top:34px}
.brand-name{font-family:"Alegreya",serif;font-size:33px;line-height:1;color:var(--ink)}
.brand-tagline{margin-top:6px;font-size:12px;line-height:16px;color:var(--ink);font-weight:500;width:210px}
.login{top:74px;height:34px;background:var(--white);display:flex;align-items:center;gap:6px;padding-left:11px;font-size:11px;color:var(--ink)}
.login.user{left:434px;width:116px}
.login.pass{left:558px;width:116px}
.login-btn{left:680px;top:74px;width:71px;height:34px;background:var(--olive);color:var(--white);display:flex;align-items:center;justify-content:center;font-size:11px;font-weight:600}

/* nav */
.main-nav{left:0;top:121px;width:768px;height:31px;display:flex;align-items:center;padding:0 16px;font-size:11.5px;color:var(--ink)}
.main-nav span{display:flex;align-items:center;gap:6px;margin-right:26px}
.main-nav .right{margin-left:auto;display:flex}
.main-nav .right span{margin-right:0;margin-left:26px}
.crumbs{left:0;top:152px;width:767px;height:28px;background:#f5f5f3;border-bottom:1px solid #e4e4e4;padding-left:19px;display:flex;align-items:center;font-size:11px;gap:4px;color:#bbb}
.ico{display:inline-block;width:8px;height:8px;border-radius:2px;background:var(--lime)}
.ico.dark{background:var(--ink)}
.ico.gray{background:#777}

/* sidebar */
.side-box{left:16px;width:144px;border-left:6px solid var(--lime);background:var(--white)}
.side-box h3{height:28px;background:var(--panel);display:flex;align-items:center;gap:6px;padding-left:12px;font-size:12.5px;font-weight:500;color:#55593a}
.side-box li{list-style:none;height:29.6px;border-bottom:1px solid var(--line);display:flex;align-items:center;gap:6px;padding-left:10px;font-size:10.5px;color:var(--ink)}
.side-box li:last-child{border-bottom:none}
.stats li{justify-content:space-between;padding-right:0}
.stats li b{font-weight:500;font-size:10px}
.new-member{left:16px;top:682px;width:144px;height:144px;background:var(--panel);text-align:center;color:var(--ink)}
.new-member h3{font-size:12.5px;font-weight:500;padding-top:16px;display:flex;justify-content:center;gap:6px;align-items:center}
.avatar{display:block;margin:5px auto 4px}
.new-member .name{font-size:12px}
.new-member .age{font-size:10.5px;margin-top:1px}
.new-member a{display:block;margin-top:6px;font-size:11px}

/* center */
.search{left:176px;top:197px;width:416px;height:89px;background:var(--panel-gray)}
.search h2{position:absolute;left:17px;top:12px;font-size:15px;font-weight:500;color:var(--ink)}
.search-field{position:absolute;left:15px;top:37px;width:287px;height:34px;background:var(--input);display:flex;align-items:center;gap:8px;padding-left:12px;font-size:12.5px;color:#5b5e44}
.search-btn{position:absolute;left:308px;top:37px;width:92px;height:34px;background:var(--button);display:flex;align-items:center;justify-content:center;font-size:12.5px;font-weight:500;color:var(--ink)}
.welcome{left:176px;top:299px;width:416px;height:371px;background:var(--panel)}
.welcome h1{position:absolute;left:17px;top:22px;font-size:48px;line-height:57px;font-weight:600;color:var(--ink);letter-spacing:.5px}
.welcome p{position:absolute;left:16px;top:141px;width:225px;font-size:12px;line-height:15.6px;color:var(--ink)}
.welcome-art{position:absolute;left:190px;top:175px;width:220px;height:170px;border-radius:50% 50% 8px 8px;background:radial-gradient(ellipse at 50% 80%,#e4e2d2 0%,#d9cfae 35%,#c9d6c4 55%,rgba(242,242,227,0) 72%)}
.subjects{left:176px;top:682px;width:416px;height:144px;border-left:6px solid var(--lime)}
.subjects h3{height:28px;background:var(--panel);display:flex;align-items:center;padding-left:13px;font-size:12px;font-weight:500;color:#55593a}
.subjects p{padding:8px 0 0 11px;font-size:10.6px;line-height:17.6px;color:#55593a}
.subjects .sep{color:#c8c8c0;margin:0 3px}

/* right */
.messenger{left:608px;top:197px;width:144px;height:126px;background:var(--panel);color:var(--ink)}
.messenger h3{display:flex;align-items:center;gap:6px;padding:12px 0 0 11px;font-size:12.5px;font-weight:500}
.messenger .note{padding:10px 10px 0 11px;font-size:9px;line-height:12.5px}
.messenger .links{padding:17px 0 0 11px;font-size:10.5px}
.messenger .status{position:absolute;left:0;bottom:0;width:144px;height:28px;background:var(--lime);display:flex;align-items:center;justify-content:center;font-size:10.5px;font-weight:500}
.promo{left:608px;top:335px;width:144px;height:307px;background:linear-gradient(180deg,#6d7f86 0%,#8b9a94 30%,#9c9a86 60%,#7f7a66 100%)}
.promo-text{position:absolute;left:9px;top:148px;color:var(--white);font-size:13.5px;line-height:18px}
.promo-text strong{display:block;font-size:29px;line-height:35px;font-weight:600;margin-top:1px}
.promo-btn{position:absolute;left:11px;top:267px;width:122px;height:25px;background:var(--lime);display:flex;align-items:center;justify-content:center;font-size:10.5px;font-weight:500;color:var(--ink)}
.online{left:608px;top:642px;width:144px;height:28px;background:var(--panel-gray);display:flex;align-items:center;gap:6px;padding-left:10px;font-size:10.5px;color:var(--ink)}

/* footer */
.site-footer{left:16px;top:927px;width:736px;display:flex;justify-content:space-between;font-size:10px;color:#999}
</style>
</head>
<body>
<div class="page">
  <header class="site-header abs">
    <div class="brand abs">
      <div class="brand-name">Kreidetafel.de</div>
      <div class="brand-tagline">Referate, Hausaufgaben und nette Leute kennen lernen</div>
    </div>
    <div class="login user abs"><svg width="9" height="9" viewBox="0 0 10 10"><circle cx="5" cy="3" r="2.5" fill="#3b3f24"/><rect x="1" y="6.5" width="8" height="3.5" rx="1.5" fill="#3b3f24"/></svg>Username</div>
    <div class="login pass abs"><svg width="9" height="10" viewBox="0 0 10 11"><path d="M2.5 5V3.5a2.5 2.5 0 0 1 5 0V5" stroke="#3b3f24" stroke-width="1.4" fill="none"/><rect x="1" y="5" width="8" height="6" rx="1" fill="#3b3f24"/></svg>Passwort</div>
    <div class="login-btn abs">Log in</div>
  </header>

  <nav class="main-nav abs">
    <span><i class="ico"></i>Startseite</span>
    <span><i class="ico"></i>Community</span>
    <span><i class="ico"></i>Referate</span>
    <div class="right">
      <span><i class="ico gray"></i>Foren</span>
      <span><i class="ico gray"></i>Mitglieder</span>
      <span><svg width="9" height="9" viewBox="0 0 10 10"><circle cx="4" cy="4" r="3" stroke="#777" stroke-width="1.3" fill="none"/><path d="M6.2 6.2 9 9" stroke="#777" stroke-width="1.3"/></svg>Flirtsuche</span>
    </div>
  </nav>
  <div class="crumbs abs"><a href="#">Foren</a>|<a href="#">Mitglieder</a>|<a href="#">Flirtsuche</a></div>

  <aside class="side-box abs" style="top:197px">
    <h3><i class="ico gray"></i>Community</h3>
    <ul>
      <li><i class="ico dark"></i>Registrieren</li>
      <li><i class="ico dark"></i>Mitglieder Login</li>
      <li><i class="ico dark"></i>Foren</li>
      <li><i class="ico dark"></i>Chat</li>
      <li><i class="ico dark"></i>Flirtsuche</li>
    </ul>
  </aside>
  <aside class="side-box abs" style="top:388px">
    <h3><i class="ico gray"></i>Schule &amp; Uni</h3>
    <ul>
      <li><i class="ico dark"></i>Hausarbeit</li>
      <li><i class="ico dark"></i>Referat</li>
    </ul>
  </aside>
  <aside class="side-box stats abs" style="top:497px">
    <h3><i class="ico gray"></i>Statistik</h3>
    <ul>
      <li>Mitglieder<b>401.324</b></li>
      <li>Männer<b>197.694</b></li>
      <li>Frauen<b>196.799</b></li>
      <li>Referate<b>12.458</b></li>
      <li>Forenbeiträge<b>3M+</b></li>
    </ul>
  </aside>
  <aside class="new-member abs">
    <h3><i class="ico dark"></i>Neue Mitglieder</h3>
    <svg class="avatar" width="40" height="40" viewBox="0 0 40 40"><circle cx="20" cy="20" r="20" fill="#c9c9c0"/><circle cx="20" cy="15" r="7" fill="#f2f2e3"/><path d="M7 31c3-6 8-8 13-8s10 2 13 8" fill="#f2f2e3"/></svg>
    <div class="name">Lunamira</div>
    <div class="age">Alter: 60 Jahre</div>
    <a href="#">Profil</a>
  </aside>

  <section class="search abs">
    <h2>Suchbegriff</h2>
    <div class="search-field"><svg width="12" height="12" viewBox="0 0 10 10"><circle cx="4" cy="4" r="3" stroke="#5b5e44" stroke-width="1" fill="none"/><path d="M6.2 6.2 9 9" stroke="#5b5e44" stroke-width="1"/></svg>Was suchst du? Hier eingeben!</div>
    <div class="search-btn">Suchen</div>
  </section>

  <section class="welcome abs">
    <h1>Hallo<br>Besucher,</h1>
    <p>Auf Kreidetafel.de findest du viele <a href="#">Referate</a>, Facharbeiten und Hausaufgaben. Solltest du einmal ein Referat zu einem Thema nicht finden, kannst du deine Frage bei uns im <a href="#">Forum</a> stellen, wo dir in der Regel schnell geholfen wird.</p>
    <div class="welcome-art" role="img" aria-label="Illustration: aufgeschlagenes Buch, aus dem bunte Papiervögel aufsteigen"></div>
  </section>

  <section class="subjects abs">
    <h3>Referate - Hausarbeiten - Hausaufgaben zu folgenden Fächern:</h3>
    <p>
      <a href="#">Deutsch</a> (2937)<span class="sep">|</span><a href="#">Englisch</a> (1113)<span class="sep">|</span><a href="#">Latein</a> (275)<span class="sep">|</span><a href="#">Franzoesisch</a> (196)<br>
      <a href="#">|Italienisch</a> (32)<span class="sep">|</span><a href="#">Griechisch</a> (28)<span class="sep">|</span><a href="#">Spanisch</a> (74)<span class="sep">|</span><a href="#">Mathematik</a> (99)<span class="sep">|</span><br>
      <a href="#">Physik</a> (481)<span class="sep">|</span><a href="#">Chemie</a> (450)<span class="sep">|</span><a href="#">Astronomie</a> (82)<span class="sep">|</span><a href="#">Geographie</a> (785)<span class="sep">|</span><br>
      <a href="#">Geschichte</a> (1870)<span class="sep">|</span><a href="#">Sozialkunde</a> (555)<span class="sep">|</span><a href="#">Wirtschaft</a> (435) <a href="#">|Recht</a> (109)<span class="sep">|</span><br>
      <a href="#">Musik</a> (448)<span class="sep">|</span><a href="#">Kunst</a> (265)<span class="sep">|</span><a href="#">Religion</a> (521)<span class="sep">|</span><a href="#">Informatik</a> (191)<span class="sep">|</span><br>
      <a href="#">Hauswirtschaft</a> (109)<span class="sep">|</span><a href="#">Sport</a> (136)<span class="sep">|</span><a href="#">Chor</a> (19)<span class="sep">|</span><a href="#">Biologie</a> (1237)
    </p>
  </section>

  <aside class="messenger abs">
    <h3><i class="ico dark"></i>LiveMessenger</h3>
    <div class="note">Diese Funktion ist nur für Mitglieder verfügbar</div>
    <div class="links">Mitglieder | Flirtsuche</div>
    <div class="status">Keine neue Nachricht</div>
  </aside>
  <aside class="promo abs" role="img" aria-label="Foto: Schüler mit Rucksack vor einem Bücherregal in einer Bibliothek">
    <div class="promo-text">Dein<br>kreidetafel.de<strong>Schon dabei?</strong></div>
    <div class="promo-btn">Registrieren</div>
  </aside>
  <div class="online abs"><i class="ico gray"></i>204 Mitglieder online</div>

  <footer class="site-footer abs">
    <span>© 2017 kreidetafel.de</span>
    <span>Hauptseite | Referate Schule - Hausarbeit | Impressum | Datenschutz | AGB</span>
  </footer>
</div>
</body>
</html>
```